Business Card Design for Mabel's Pantry

We make food for dogs.
Business Card Design (using the logo designed by you). Our Brand color is a bright canary yellow. For example our signage is predominantly yellow, with the logo in black. I'd like the card also to use that imagery.
Feel free to use the two sides creatively.
Vertical Design is also great.

Industry/Entity Type

Pet food

Contact Information for Business Card

Name, email, website, phone no

Font styles to use
Sans Serif

Colors
59FF00
82FF00
B8FF75
E3FFCB
F4FFEA
FFF300
FFF600
FEFA6F
FFFEC7
FFFEE8

Requirements
Nice to have
• A graphic in the same brush stroke style of the logo shoeing a doggy bowl of food

```html
<!DOCTYPE html>
<html lang="en">
<head>
<meta charset="utf-8">
<title>Mabel's Pantry — Business Card</title>
<link href="https://fonts.googleapis.com/css2?family=Roboto:wght@400;500;700&display=swap" rel="stylesheet">
<style>
  :root {
    --backdrop: #3a3a3a;
    --card-yellow: #fee45a;
    --ink: #111111;
    --emboss: #f2d446;
  }
  * { box-sizing: border-box; margin: 0; padding: 0; }
  html, body {
    width: 1200px;
    height: 1015px;
    overflow: hidden;
    background: var(--backdrop);
    font-family: "Roboto", Arial, sans-serif;
  }
  .stage {
    width: 1200px;
    height: 1015px;
    display: flex;
    flex-direction: column;
    align-items: center;
    justify-content: center;
    gap: 40px;
  }
  .card {
    width: 820px;
    height: 460px;
    background: var(--card-yellow);
    position: relative;
    color: var(--ink);
  }
  .card-front {
    display: flex;
    align-items: center;
    justify-content: center;
  }
  .brand {
    display: flex;
    align-items: center;
    gap: 18px;
    font-weight: 700;
    font-size: 64px;
    letter-spacing: 1px;
    text-transform: uppercase;
    color: var(--ink);
  }
  .brand-dot {
    width: 30px;
    height: 30px;
    border-radius: 50%;
    background: currentColor;
  }
  .card-back .brand {
    position: absolute;
    right: 46px;
    top: 150px;
    font-size: 50px;
    color: var(--emboss);
  }
  .contact {
    position: absolute;
    left: 70px;
    top: 70px;
  }
  .person-name {
    font-weight: 700;
    font-size: 26px;
    letter-spacing: 0.5px;
    text-transform: uppercase;
  }
  .person-role {
    font-size: 16px;
    letter-spacing: 0.5px;
    text-transform: uppercase;
    margin-top: 2px;
  }
  .address {
    font-style: normal;
    font-size: 20px;
    line-height: 1.3;
    margin: 40px 0 0 36px;
  }
  .channels {
    list-style: none;
    margin: 44px 0 0 70px;
    font-size: 20px;
    line-height: 1.3;
  }
  .channels li {
    display: flex;
    align-items: center;
    gap: 8px;
  }
  .channels svg { width: 16px; height: 16px; flex: none; }
</style>
</head>
<body>
<main class="stage">
  <section class="card card-front" aria-label="Card front">
    <div class="brand"><span class="brand-dot"></span>Mabel's Pantry</div>
  </section>

  <section class="card card-back" aria-label="Card back">
    <div class="contact">
      <h1 class="person-name">Daniel Hart</h1>
      <p class="person-role">Managing Director</p>
      <address class="address">
        88 Orchard Lane,<br>
        Springfield 20417<br>
        Country
      </address>
      <ul class="channels">
        <li>
          <svg viewBox="0 0 16 16" aria-hidden="true"><path d="M3 1.5l3 .5 1 3-1.8 1.3a9 9 0 0 0 4.5 4.5L11 9l3 1 .5 3-2 1.5C6.5 14 2 9.5 1.5 3.5z" fill="var(--ink)"/></svg>
          044-987 654 321
        </li>
        <li>
          <svg viewBox="0 0 16 16" aria-hidden="true"><rect x="1" y="3" width="14" height="10" fill="var(--ink)"/><path d="M1 3l7 5.5L15 3" fill="none" stroke="var(--card-yellow)" stroke-width="1.4"/></svg>
          hello@mabelspantry.com
        </li>
        <li>
          <svg viewBox="0 0 16 16" aria-hidden="true"><circle cx="8" cy="8" r="7" fill="var(--ink)"/><g fill="none" stroke="var(--card-yellow)" stroke-width="1"><ellipse cx="8" cy="8" rx="3" ry="7"/><path d="M1 8h14M2.5 4.5h11M2.5 11.5h11"/></g></svg>
          www.mabelspantry.com
        </li>
      </ul>
    </div>
    <div class="brand"><span class="brand-dot"></span>Mabel's Pantry</div>
  </section>
</main>
</body>
</html>
```